Tall-Anchor Brochure

We would like a 3 panel layout format with copy on both sides and on each panel, (we will provide content).

We are Tall-Anchor and we work with business owners to achieve measurable growth and success based on 6 Core Pillars Of Momentum and (S.B.L) 90 Day Steady Build Ledger. We also work with the business leader and individuals within the organization with personal development.

We would like the brochure to have a corporate feel, but warm and inviting. We don't want a hard or aggressive feel.

We would like it to be available for pdf upload and physical print formats.

The winning design will also be invited to design a header for our website as well. The header will be consistent with the brochure, so please keep that in mind during your creative process.

I am enclosing a transparent copy of our company logo along with content for the brochure.

Thank you in advance for your consideration!

Gordon and Moira
Updates

Sorry, but we forgot to include the front cover text.

It will read as follows,

Do you know the 6 Core Pillars Of Momentum  that are crucial to the success of any business today?

Also, please add the following to the back page

Website: www.tall-anchor.example
Resource Centre: www.taresources.example 
Phone: +44 (0) 7812056417
Email: info@tall-anchor.example

Follow us on (please insert Facebook, Linkedin and YouTube logo)

I have uploaded a pdf format of brochure text.

Hello designers. I wanted to give some further input to help the process. Although the brochure is to target business, we don't want to over do it with corporate professioanls in all the photos. If there is an opportunity to incorporate photos of small business owners like, a butcher, baker, chef, flower shop etc. This would hopefully help us make an immpression to all small business owners.

Thank you, and good luck!

Gordon and Moira  

Reason: A few designers have come come on board last minute. So I'd like to give everyone the same opportunity to respond. Sincerely, Gordon

Target Market(s)

Small Business Owners searching for new ways to grow their business in the UK and Republic Of Ireland.

Industry/Entity Type

Business

```html
<!DOCTYPE html>
<html lang="en">
<head>
<meta charset="utf-8">
<title>Tall-Anchor Brochure – Inside Spread</title>
<link rel="stylesheet" href="https://fonts.googleapis.com/css2?family=Montserrat:wght@600;700;800&family=Arimo:wght@400;700&display=swap">
<style>
  :root {
    --page-bg: #e9e9eb;
    --navy-deep: #1b1d3d;
    --navy-mid: #2b2d52;
    --slate-top: #5a5c78;
    --slate-mid: #3a3c5e;
    --accent-purple: #8c3d8e;
    --heading-grey: #a3a3ae;
    --text-light: #d9d9e2;
    --text-white: #ffffff;
    --rule: rgba(255,255,255,0.35);
    --photo-light: #eef2f6;
    --photo-mid: #c9d3df;
    --photo-warm: #e7d4c8;
  }
  * { margin: 0; padding: 0; box-sizing: border-box; }
  html, body { width: 1200px; height: 1000px; overflow: hidden; }
  body {
    background: var(--page-bg);
    font-family: "Arimo", Arial, sans-serif;
    position: relative;
  }
  .brochure {
    position: absolute;
    left: 60px; top: 110px;
    width: 1080px; height: 780px;
    box-shadow: 0 18px 40px rgba(0,0,0,0.25);
    overflow: hidden;
  }
  .brochure__photo {
    position: absolute; inset: 0;
    background:
      radial-gradient(ellipse at 70% 65%, var(--photo-warm) 0%, transparent 35%),
      radial-gradient(ellipse at 30% 85%, var(--photo-warm) 0%, transparent 30%),
      linear-gradient(160deg, var(--photo-mid) 0%, var(--photo-light) 45%, #ffffff 70%, var(--photo-mid) 100%);
  }
  .brochure__bands { position: absolute; inset: 0; }
  .fold {
    position: absolute; top: 0; width: 1px; height: 100%;
    background: rgba(0,0,0,0.08);
  }
  .panel {
    position: absolute; top: 0; width: 360px;
    color: var(--text-light);
  }
  .panel--solutions { left: 0; padding: 38px 34px 0 34px; }
  .panel--start { left: 360px; padding: 36px 34px 0; text-align: center; }
  .panel--next { left: 720px; padding: 36px 34px 0; }

  .section-title {
    font-family: "Montserrat", sans-serif;
    font-weight: 700; font-size: 17px;
    color: var(--text-white); margin-bottom: 14px;
  }
  .body-copy {
    font-size: 13px; line-height: 1.45;
    text-align: justify; color: var(--text-light);
  }
  .service-list {
    list-style: none; margin: 14px 0 18px;
  }
  .service-list li {
    font-weight: 700; font-size: 13px; line-height: 1.8; color: var(--text-white);
  }
  .divider { border: 0; border-top: 1px solid var(--rule); margin: 0 0 26px; }
  .link { color: var(--accent-purple); }

  .big-heading {
    font-family: "Montserrat", sans-serif;
    font-weight: 800; font-size: 44px; line-height: 0.95;
    letter-spacing: 1px; text-transform: uppercase;
  }
  .big-heading .grey { color: var(--heading-grey); display: block; }
  .big-heading .purple { color: var(--accent-purple); display: block; }

  .start-icon { display: block; margin: 0 auto 14px; }
  .start-line { font-size: 14px; color: var(--text-light); margin-top: 20px; }
  .start-line + .start-line { margin-top: 2px; }
  .start-url { font-family: "Montserrat", sans-serif; font-weight: 700; font-size: 20px; color: var(--text-white); }
  .start-phone { font-family: "Montserrat", sans-serif; font-weight: 700; font-size: 27px; color: var(--text-white); letter-spacing: 1px; }
  .start-cta { font-family: "Montserrat", sans-serif; font-weight: 800; font-size: 23px; color: var(--text-white); letter-spacing: 0.5px; }
  .start-small { font-size: 13px; color: var(--text-light); }
  .panel--start .body-copy { margin-top: 8px; }

  .next-head { display: flex; align-items: center; gap: 10px; margin-bottom: 18px; }
  .next-head .big-heading { font-size: 40px; }
  .pillar-list { list-style: none; margin: 6px 0 16px; }
  .pillar-list li { font-weight: 700; font-size: 13px; line-height: 1.9; color: var(--text-white); }
  .pillar-list li::before { content: "- "; }
  .strong { font-weight: 700; color: var(--text-white); }
</style>
</head>
<body>
  <div class="brochure">
    <div class="brochure__photo" role="img" aria-label="Photograph of two hands over printed business charts, one holding a pen"></div>

    <svg class="brochure__bands" width="1080" height="780" viewBox="0 0 1080 780" aria-hidden="true">
      <defs>
        <clipPath id="wave">
          <path d="M0 0 H1080 V430 C940 470 800 500 660 520 C500 545 320 600 0 610 Z"/>
        </clipPath>
        <linearGradient id="band-left" x1="0" y1="0" x2="0" y2="1">
          <stop offset="0" stop-color="#4c4e6b"/>
          <stop offset="1" stop-color="#262846"/>
        </linearGradient>
        <linearGradient id="band-mid" x1="0" y1="0" x2="0" y2="1">
          <stop offset="0" stop-color="#5d5f7c"/>
          <stop offset="0.5" stop-color="#2e3054"/>
          <stop offset="1" stop-color="#1f2142"/>
        </linearGradient>
        <linearGradient id="band-right" x1="0" y1="0" x2="0" y2="1">
          <stop offset="0" stop-color="#23254a"/>
          <stop offset="1" stop-color="#1a1c3b"/>
        </linearGradient>
      </defs>
      <g clip-path="url(#wave)">
        <rect x="0" y="0" width="360" height="780" fill="url(#band-left)"/>
        <rect x="360" y="0" width="360" height="780" fill="url(#band-mid)"/>
        <rect x="720" y="0" width="360" height="780" fill="url(#band-right)"/>
      </g>
    </svg>

    <div class="fold" style="left:360px"></div>
    <div class="fold" style="left:720px"></div>

    <section class="panel panel--solutions">
      <h2 class="section-title">Business Solutions</h2>
      <p class="body-copy">In addition to the Total Business Analysis / S.B.L package, we also offer other business solutions which can be used individually or bundled together to create a package suitable for your needs.</p>
      <ul class="service-list">
        <li>One on one business mentoring</li>
        <li>Marketing strategies</li>
        <li>Sales training (individual or group)</li>
        <li>Management training (individual or group)</li>
        <li>Customer service training (individual or group)</li>
      </ul>
      <hr class="divider">
      <h2 class="section-title">Resource Centre</h2>
      <p class="body-copy">At Tall-Anchor, we are dedicated to providing current and relevant information through our resource centre <span class="link">www.taresources.example</span> where you will find access to videos, reports, statistics and newsletters. You will also find details on upcoming events, such as webinars, workshops and online training.</p>
    </section>

    <section class="panel panel--start">
      <svg class="start-icon" width="64" height="56" viewBox="0 0 64 56" aria-hidden="true">
        <g fill="var(--heading-grey)">
          <circle cx="32" cy="14" r="6"/>
          <path d="M23 22 H41 L38 40 H35 V54 H29 V40 H26 Z"/>
        </g>
        <g fill="var(--accent-purple)">
          <path d="M2 2 L16 4 L11 7 L19 15 L15 19 L7 11 L4 16 Z"/>
          <path d="M62 2 L60 16 L57 11 L49 19 L45 15 L53 7 L48 4 Z"/>
          <path d="M2 54 L4 40 L7 45 L15 37 L19 41 L11 49 L16 52 Z"/>
          <path d="M62 54 L48 52 L53 49 L45 41 L49 37 L57 45 L60 40 Z"/>
        </g>
      </svg>
      <h2 class="big-heading"><span class="grey">Getting</span><span class="purple">Started</span></h2>
      <p class="start-line">The first step is to visit</p>
      <p class="start-url">www.tall-anchor.example</p>
      <p class="start-small">or call</p>
      <p class="start-phone">07812056417</p>
      <p class="start-small">to book your</p>
      <p class="start-cta">FREE CONSULTATION.</p>
      <p class="body-copy">This will be an opportunity for you to think about where you want your business to go and for us to establish how we can help you get there.</p>
    </section>

    <section class="panel panel--next">
      <div class="next-head">
        <svg width="60" height="62" viewBox="0 0 60 62" aria-hidden="true">
          <path d="M24 2 A14 14 0 1 1 24 30 L18 36 L19 28 A14 14 0 0 1 24 2 Z" fill="var(--accent-purple)"/>
          <text x="24" y="23" text-anchor="middle" font-family="Montserrat, sans-serif" font-weight="800" font-size="18" fill="#1b1d3d">?</text>
          <circle cx="14" cy="42" r="6" fill="var(--heading-grey)"/>
          <path d="M2 62 C2 52 7 49 14 49 C21 49 26 52 26 62 Z" fill="var(--heading-grey)"/>
        </svg>
        <h2 class="big-heading"><span class="grey">After</span><span class="purple">That?</span></h2>
      </div>
      <p class="body-copy">We will carry out a business analysis based on <span class="strong">The 6 Core Pillars Of Momentum:</span></p>
      <ul class="pillar-list">
        <li>Your Brand</li>
        <li>Sales</li>
        <li>Your People</li>
        <li>Product and Service</li>
        <li>Psychology and Skills</li>
        <li>Finance</li>
      </ul>
      <p class="body-copy">We then provide you with a detailed report and work with you to create and implement your Steady Build Ledger (S.B.L). This is a 90 day plan, customized for your business and designed so you can start seeing positive and measurable results immediately.</p>
    </section>
  </div>
</body>
</html>
```